Sleek business card design for digital agency.

Brief document attached for detailed description and inspiration. Looking for a minimalist sleek, cool, modern business card design.

Industry/Entity Type

Digital

```html
<!DOCTYPE html>
<html lang="en">
<head>
<meta charset="utf-8">
<title>Flint Studio – Business Card Options</title>
<link rel="stylesheet" href="https://fonts.googleapis.com/css2?family=Questrial&display=swap">
<style>
  :root {
    --sheet: #ffffff;
    --caption: #9a9a9a;
    --card-base: #07070f;
    --card-glow: rgba(20, 90, 45, 0.55);
    --ink-white: #f2f2f2;
    --ink-soft: #d8d8d8;
    --mark-grey: #6e6e72;
    --mark-faint: #4a4a50;
    --mark-green: #22d37a;
    --illo-grey: rgba(150, 150, 160, 0.32);
  }
  * { margin: 0; padding: 0; box-sizing: border-box; }
  html, body {
    width: 1200px; height: 1200px; overflow: hidden;
    background: var(--sheet);
    font-family: "Questrial", "Century Gothic", sans-serif;
  }
  .sheet { position: relative; width: 1200px; height: 1200px; }

  .caption {
    position: absolute; width: 544px; text-align: center;
    font-size: 19px; color: var(--caption);
  }
  .card {
    position: absolute; width: 544px; height: 313px; overflow: hidden;
    background:
      radial-gradient(ellipse 45% 55% at 50% 62%, var(--card-glow), transparent 75%),
      var(--card-base);
  }
  .col-left { left: 24px; }
  .col-right { left: 631px; }
  .row-1 { top: 74px; }
  .row-2 { top: 440px; }
  .row-3 { top: 811px; }
  .cap-1 { top: 46px; }
  .cap-2 { top: 408px; }
  .cap-3 { top: 776px; }

  .wordmark {
    position: absolute; left: 0; width: 100%; text-align: center;
    top: 132px; font-size: 40px; letter-spacing: 1px;
  }
  .wordmark--grey { color: var(--mark-grey); }
  .wordmark--green { color: var(--mark-green); }
  .wordmark--faint {
    width: auto; left: 58px; top: 204px; font-size: 34px; color: var(--mark-faint);
  }

  .name {
    position: absolute; left: 161px; top: 52px;
    font-size: 29px; letter-spacing: 1.5px; color: var(--ink-white);
  }
  .role {
    position: absolute; left: 161px; top: 104px;
    font-size: 17px; letter-spacing: 2px; color: var(--ink-white);
  }
  .drink {
    position: absolute; left: 161px; top: 126px;
    font-size: 10px; letter-spacing: 2.4px; color: var(--ink-soft);
  }
  .contact {
    position: absolute; left: 358px; top: 164px;
    list-style: none; font-size: 11px; line-height: 14.2px; color: var(--ink-white);
  }

  .illustration { position: absolute; }
  .illustration--outline {
    left: 10px; top: 0; width: 380px; height: 313px;
    background: radial-gradient(ellipse 50% 50% at 30% 62%, var(--illo-grey), transparent 72%);
  }
  .illustration--spectrum {
    left: 0; top: 0; width: 440px; height: 313px; opacity: 0.55;
    background: linear-gradient(20deg, #d11414 10%, #e6c21a 30%, #2bb44a 55%, #2a6bd6 75%, #b12ad6 95%);
    -webkit-mask: radial-gradient(ellipse 60% 60% at 40% 55%, #000 20%, transparent 75%);
            mask: radial-gradient(ellipse 60% 60% at 40% 55%, #000 20%, transparent 75%);
  }
  .illustration--solid {
    left: 40px; top: 0; width: 420px; height: 313px;
    background: radial-gradient(ellipse 48% 55% at 28% 70%, rgba(130, 130, 138, 0.55), transparent 72%);
  }
</style>
</head>
<body>
<main class="sheet">

  <p class="caption col-left cap-1">Logo is spot UV+volume stamping</p>
  <section class="card col-left row-1" aria-label="Card front, embossed">
    <p class="wordmark wordmark--grey">Flint Studio</p>
  </section>

  <p class="caption col-right cap-1">Shrimp is spot UV</p>
  <section class="card col-right row-1" aria-label="Card back, outline shrimp">
    <div class="illustration illustration--outline" role="img" aria-label="Thin grey line drawing of a shrimp with long flowing antennae"></div>
    <p class="name">DANIEL HART</p>
    <p class="role">MARKETING DIRECTOR</p>
    <p class="drink">DRINK ORDER: G&amp;T WITH CUCUMBER</p>
    <ul class="contact">
      <li>Level 2, 18 Harbour Ln</li>
      <li>East Marlow NSW 2000</li>
      <li>0400 000 123</li>
      <li>03 9000 1234</li>
      <li>DHART@FLINTSTUDIO.COM</li>
      <li>@DHART82</li>
      <li>FACEBOOK.COM/FLINTSTUDIO</li>
    </ul>
  </section>

  <p class="caption col-left cap-2">Logo is spot UV</p>
  <section class="card col-left row-2" aria-label="Card front, green">
    <p class="wordmark wordmark--green">Flint Studio</p>
  </section>

  <section class="card col-right row-2" aria-label="Card back, spectrum shrimp">
    <div class="illustration illustration--spectrum" role="img" aria-label="Rainbow-coloured line drawing of a shrimp with long flowing antennae"></div>
    <p class="name">DANIEL HART</p>
    <p class="role">MARKETING DIRECTOR</p>
    <p class="drink">DRINK ORDER: G&amp;T WITH CUCUMBER</p>
    <ul class="contact">
      <li>Level 2, 18 Harbour Ln</li>
      <li>East Marlow NSW 2000</li>
      <li>0400 000 123</li>
      <li>03 9000 1234</li>
      <li>DHART@FLINTSTUDIO.COM</li>
      <li>@DHART82</li>
      <li>FACEBOOK.COM/FLINTSTUDIO</li>
    </ul>
  </section>

  <p class="caption col-left cap-3">Shrimp is spot UV</p>
  <section class="card col-left row-3" aria-label="Card front, solid shrimp">
    <div class="illustration illustration--solid" role="img" aria-label="Solid grey shrimp silhouette with long flowing antennae"></div>
  </section>

  <p class="caption col-right cap-3">Logo is spot UV</p>
  <section class="card col-right row-3" aria-label="Card back with faint name">
    <p class="wordmark wordmark--faint">Flint Studio</p>
    <p class="name">DANIEL HART</p>
    <p class="role">MARKETING DIRECTOR</p>
    <p class="drink">DRINK ORDER: G&amp;T WITH CUCUMBER</p>
    <ul class="contact">
      <li>Level 2, 18 Harbour Ln</li>
      <li>East Marlow NSW 2000</li>
      <li>0400 000 123</li>
      <li>03 9000 1234</li>
      <li>DHART@FLINTSTUDIO.COM</li>
      <li>@DHART82</li>
      <li>FACEBOOK.COM/FLINTSTUDIO</li>
    </ul>
  </section>

</main>
</body>
</html>
```